Luxury Eye Cream Label

Velmora Skin is developing a line of luxury dermatology creams designed to improve and treat various skin conditions and esthetic problems.
All creams are handmade by registered pharmacies according to patient needs, on the same day of the order. (meaning the creams are not premade. the creams are freshly made without any preservatives or stabilizers.)
The labels are two. One for the upper lid of an aluminum container 4.0 cm. in diameter containing company logo and description of the cream. The other one is for the bottom of the container 4.0 in diameter containing pharmacy information.
The label should convey professional, MD, and luxury feel.
(Upper Lid Label)
Logo of velmora skin
EYE CARE CREAM - intensive
Doctor Series
handmade . Doctor formulated . registered Pharmacy . highest ethical standards . (in a circular pattern on the label)
Ingredients: Marigold extract, Witch Hazel Distillate, Water, Glycerin, Stearyl Alcohol, Wheat Germ Oil, Polysorbate 60, Sesame Oil, Myristyl Myristate, Cetyl Alcohol, Sorbitan Stearate, Phenoxyethanol, Calendula Extract, Cornflower Extract, Sodium Alginate, Sodium Citrate, Mica, Vit. C, Vit. E.
Please, adhere to the above content, and dimension of the label of 4 cm in diameter. Also, please view it to scale. This is a relatively small container, aluminum ½ ounce (15ml) cream.
The Bottom of the Jar will have a label with the following information. This is obligatory, because of regulatory requirements for any product prepared by a pharmacy.
I understand that the space is limited. The background should be a lighter color, and the pharmacist will hand write the information (with a darker color marker).
EXTERNAL USE
Pharmacy: Pelaro, 18 Blvd. Ts. Orlinov, Sofia 1157, ph. 02 9473615
Rx No. Date
Patient Name age
Pharmacist Good until:
Please, view it to scale of 4 cm in diameter (which is the actual label of the Face Cream Intense), so you will have a better feeling of the design.
Thank you so much.

```html
<!DOCTYPE html>
<html lang="en">
<head>
<meta charset="utf-8">
<title>Velmora Skin – Eye Care Cream Labels</title>
<link rel="stylesheet" href="https://fonts.googleapis.com/css2?family=Lato:wght@300;400&family=Open+Sans:wght@400&display=swap">
<style>
  :root {
    --label-black: #0b0a0a;
    --gold: #d4b06a;
    --gold-bar: #d6b56e;
    --ink-white: #f4f1ea;
    --ink-dark: #1a1612;
    --page: #ffffff;
  }
  html, body {
    margin: 0;
    padding: 0;
    width: 1200px;
    height: 619px;
    overflow: hidden;
    background: var(--page);
  }
  .canvas {
    position: relative;
    width: 1200px;
    height: 619px;
  }
  .label {
    position: absolute;
    top: 28px;
    width: 564px;
    height: 564px;
    border-radius: 50%;
    background: var(--label-black);
    overflow: hidden;
    font-family: "Open Sans", sans-serif;
    color: var(--ink-white);
  }
  .label--lid { left: 14px; }
  .label--base { left: 604px; }
  .label__rings {
    position: absolute;
    inset: 0;
  }
  .centered {
    position: absolute;
    left: 0;
    width: 100%;
    text-align: center;
    margin: 0;
  }
  /* Lid label */
  .brand {
    top: 112px;
    font-family: "Lato", sans-serif;
    font-weight: 400;
    font-size: 29px;
    color: var(--gold);
    display: flex;
    justify-content: center;
    align-items: center;
    gap: 10px;
  }
  .brand__dot {
    width: 14px;
    height: 14px;
    border-radius: 50%;
    background: var(--gold);
  }
  .product-name {
    top: 180px;
    font-family: "Lato", sans-serif;
    font-weight: 400;
    font-size: 27px;
    letter-spacing: 0.3px;
  }
  .product-variant {
    top: 221px;
    font-size: 21px;
    letter-spacing: 1.5px;
  }
  .series {
    top: 282px;
    font-family: "Lato", sans-serif;
    font-size: 21px;
    color: var(--gold);
  }
  .divider {
    position: absolute;
    left: 76px;
    top: 305px;
    width: 412px;
    height: 2px;
    background: var(--gold);
  }
  .ingredients {
    top: 357px;
    font-size: 12px;
    line-height: 19.3px;
  }
  /* Base label */
  .usage {
    top: 131px;
    font-size: 12px;
  }
  .pharmacy {
    top: 185px;
    font-size: 12.5px;
    line-height: 25px;
  }
  .rx-field {
    position: absolute;
    left: 94px;
    width: 378px;
    height: 47px;
    background: var(--gold-bar);
    color: var(--ink-dark);
    font-size: 16px;
    line-height: 47px;
  }
  .rx-field--top { top: 258px; }
  .rx-field--bottom { top: 321px; }
  .rx-field span {
    position: absolute;
    top: 0;
  }
  .rx-field .field-left { left: 9px; }
  .rx-field .field-right { left: 224px; }
  .sign-field {
    position: absolute;
    left: 151px;
    font-size: 14px;
  }
  .sign-field--until { top: 403px; }
  .sign-field--pharmacist { top: 441px; }
</style>
</head>
<body>
<main class="canvas">

  <section class="label label--lid" aria-label="Upper lid label">
    <svg class="label__rings" viewBox="0 0 564 564" width="564" height="564">
      <defs>
        <path id="claim-path" d="M 101.7 462.3 A 255 255 0 1 1 462.3 462.3 A 255 255 0 0 1 101.7 462.3"/>
      </defs>
      <circle cx="282" cy="282" r="236" fill="none" stroke="var(--gold)" stroke-width="2.5"/>
      <text fill="var(--ink-white)" font-family="Open Sans, sans-serif" font-size="18" textLength="1560" lengthAdjust="spacing">
        <textPath href="#claim-path">Handmade . Doctor formulated . Registered Pharmacy . Highest Ethical Standards.</textPath>
      </text>
    </svg>

    <div class="centered brand"><span class="brand__dot"></span><span>velmora skin</span></div>
    <h1 class="centered product-name">EYE CARE CREAM</h1>
    <p class="centered product-variant">intensive</p>
    <p class="centered series">Doctor Series</p>
    <div class="divider"></div>
    <p class="centered ingredients">
      Ingredients: Marigold extract, Witch Hazel Distillate,<br>
      Water, Glycerin, Stearyl Alcohol, Wheat Germ Oil,<br>
      Polysorbate60,&nbsp; Sesame Oil, MyristylMyristate, Cetyl<br>
      Alcohol, Sorbitan Stearate, Phenoxyethanol, Calendula<br>
      Extract, Cornflower Extract, Sodium Alginate, Sodium<br>
      Citrate, Mica, Vit. C, Vit. E.
    </p>
  </section>

  <section class="label label--base" aria-label="Bottom pharmacy label">
    <svg class="label__rings" viewBox="0 0 564 564" width="564" height="564">
      <circle cx="282" cy="282" r="254" fill="none" stroke="var(--gold)" stroke-width="5" stroke-dasharray="9 7"/>
      <circle cx="282" cy="282" r="240" fill="none" stroke="var(--gold)" stroke-width="2"/>
    </svg>

    <p class="centered usage">EXTERNAL USE</p>
    <p class="centered pharmacy">
      Pharmacy: Pelaro, 18 Blvd. Ts. Orlinov, Sofia 1157,<br>
      ph. 02 9473615
    </p>

    <div class="rx-field rx-field--top">
      <span class="field-left">Rx No:</span>
      <span class="field-right">Date:</span>
    </div>
    <div class="rx-field rx-field--bottom">
      <span class="field-left">For:</span>
      <span class="field-right">Age:</span>
    </div>

    <p class="sign-field sign-field--until">Good Until:</p>
    <p class="sign-field sign-field--pharmacist">Pharmacist:</p>
  </section>

</main>
</body>
</html>
```